Maple Lane Cafe & Market Squarespace Website Files

We need a Squarespace website for a new company called "Maple Lane Cafe & Market".

The company is committed to providing the highest quality, fresh and natural food, health and wellness products.

We would like to see designs that use the colors of our logo. Please provide graphic design and layout for the site.

The final design should communicate health and wellness.

Target Market(s)

Maple Lane Cafe & Market is a new company that will offer customers organic and
locally grown produce, chemical and preservative-free groceries, cruelty-free body care and eco-household products. Additionally, our kitchen will offer healthy lunch and dinner options emphasizing organic and whole food options, recognizing the trend within the restaurant industry for the demand for healthy cuisine. The restaurant will procure local foods when possible, reducing dependence on fossil fuels used for transportation. All of our products are healthy alternatives to the products available at conventional grocery chains.

Located in the heart of the growing Birchwood Avenue section of Lewiston, NY, the
marketplace will serve a community of residents in Lewiston, residents in
Niagara Falls, and residents in Niagara Falls, Ontario, Canada.

The creation of the marketplace is in response to the growing demand in the community for a local natural food store.

Industry/Entity Type

Cafe

Font styles to use
Sans Serif

Colors
00a990
faa54b
87cfc7
f37122

Requirements
Must have
• Home page, Events, Cafe Menu, Marketplace Products, Health Info, News, Recipes, Contact Us (Email form and Social Media links), Newsletter sign up.
Nice to have
• Order Online
Should not have
• (Can't think of anything right now :-)

```html
<!DOCTYPE html>
<html lang="en">
<head>
<meta charset="utf-8">
<title>Maple Lane Cafe &amp; Market</title>
<link href="https://fonts.googleapis.com/css2?family=Cinzel:wght@400;600;700&family=Open+Sans:wght@400;600&family=Bree+Serif&family=Lora:ital,wght@0,700;1,400&display=swap" rel="stylesheet">
<style>
:root{
  --teal:#00a990;
  --teal-light:#2fc6ab;
  --teal-dark:#0b9a80;
  --mint:#87cfc7;
  --orange:#f37122;
  --amber:#faa54b;
  --ink:#2a2a2a;
  --text:#555;
  --soft:#f7f7f7;
  --line:#e6e6e6;
  --white:#fff;
}
*{margin:0;padding:0;box-sizing:border-box}
html,body{width:1200px;height:2719px;overflow:hidden;background:var(--white)}
body{position:relative;font-family:"Open Sans",Arial,sans-serif;color:var(--text)}
.abs{position:absolute}
.section-title{position:absolute;left:0;width:1200px;text-align:center;font-family:"Cinzel",Georgia,serif;font-weight:600;font-size:30px;color:var(--ink);letter-spacing:1px}
.btn{position:absolute;display:flex;align-items:center;justify-content:center;color:var(--white);background:linear-gradient(var(--teal-light),var(--teal-dark));border-radius:4px;font-size:17px;font-weight:600}
.photo{position:absolute}

/* header */
.brand{left:82px;top:40px;display:flex;align-items:center;gap:14px}
.brand-mark{width:46px;height:46px;border-radius:50%;background:var(--amber)}
.brand-name{font-weight:600;font-size:26px;color:var(--teal);line-height:1.15}
.account{right:58px;top:118px;font-family:"Cinzel",serif;font-weight:600;font-size:11.5px;color:#333;letter-spacing:.5px}
.account span{margin:0 10px;color:#888}
.nav{left:0;top:156px;width:1200px;height:56px;background:linear-gradient(var(--teal-light),var(--teal-dark));display:flex;justify-content:space-between;align-items:center;padding:0 58px}
.nav a{font-family:"Cinzel",serif;font-weight:600;font-size:15px;color:var(--white);text-decoration:none;letter-spacing:.3px}

/* hero */
.hero{left:0;top:212px;width:1200px;height:546px;background:radial-gradient(circle at 70% 25%,#f3ddc9,#e9efd9 30%,#c7d8a8 60%,#7f9c4c 85%,#c24a2a)}
.hero-band{left:0;top:520px;width:1200px;height:238px;background:rgba(60,60,60,.7)}
.hero-title{left:0;top:548px;width:1200px;text-align:center;font-family:"Cinzel",serif;font-weight:600;font-size:30px;color:var(--white);letter-spacing:1px}
.hero-sub{left:0;top:600px;width:1200px;text-align:center;font-size:22px;color:var(--white)}
.dots{left:565px;top:720px;display:flex;gap:15px}
.dots i{width:13px;height:13px;border-radius:50%;background:#ddd}
.dots i.on{background:var(--teal-light)}

/* features */
.feature-panel{left:103px;top:816px;width:1097px;height:378px;background:var(--soft)}
.feature-label{width:299px;text-align:center;font-size:22px;color:#222;top:1061px}
.rule{left:0;width:1200px;height:1px;background:var(--line)}

/* products */
.product-name{width:261px;text-align:center;font-family:"Lora",serif;font-weight:700;font-size:15.5px;color:#222;top:1453px;line-height:1.3}
.product-price{width:261px;text-align:center;font-size:17px;color:#333;top:1503px}

/* welcome */
.welcome{left:0;top:1640px;width:1200px;height:459px;background:var(--soft);border-top:1px solid var(--line);border-bottom:1px solid var(--line)}
.video{left:60px;top:1767px;width:516px;height:287px;background:radial-gradient(circle at 40% 45%,#f0c060,#d89a3a 35%,#9a6a3c 60%,#5e4028)}
.video-bar{left:72px;top:2010px;width:494px;height:34px;background:rgba(0,0,0,.75);border-radius:3px}
.video-track{left:142px;top:2024px;width:320px;height:6px;background:#555;border-radius:3px}
.video-fill{left:142px;top:2024px;width:95px;height:6px;background:var(--teal-light);border-radius:3px}
.video-side{left:527px;display:flex;align-items:center;justify-content:center;width:40px;height:30px;background:rgba(0,0,0,.8);border-radius:3px}
.welcome-head{left:596px;top:1764px;width:545px;font-family:"Bree Serif",serif;font-weight:400;font-size:20px;color:#222;line-height:1.4}
.welcome-copy{left:596px;width:540px;font-size:15px;line-height:1.6;color:#666}

/* testimonial */
.avatar{left:60px;top:2217px;width:127px;height:127px;border-radius:50%;background:radial-gradient(circle at 50% 40%,#f4dcc0,#e2b07e 55%,#c7845a)}
.quote-mark{left:218px;top:2210px;font-family:Georgia,serif;font-size:80px;color:#d8d8d8;line-height:1}
.quote-text{left:277px;top:2238px;width:865px;font-size:13px;line-height:1.65;color:#666}
.quote-name{left:277px;top:2303px;font-family:"Lora",serif;font-style:italic;font-size:15px;color:#222}

/* footer */
.footer{left:0;top:2396px;width:1200px;height:232px;background:#f1f1f1}
.foot-head{top:2435px;font-family:"Lora",serif;font-weight:700;font-size:21px;color:#222}
.foot-list{top:2480px;list-style:none;font-size:13px;line-height:22px;color:#333}
.mail-input{left:459px;top:2485px;width:239px;height:40px;background:var(--white);border:1px solid #cfcfcf;border-radius:3px;font-size:12px;color:#888;display:flex;align-items:center;padding-left:14px}
.social{left:912px;top:2483px;display:flex;gap:3px}
.social i{width:30px;height:30px;border-radius:4px;background:var(--mint)}
.copyright-bar{left:0;top:2628px;width:1200px;height:91px;background:linear-gradient(#e9e9e9,#f8f8f8)}
.copyright{left:0;top:2661px;width:1200px;text-align:center;font-size:13px;font-weight:600;color:#222}
</style>
</head>
<body>

<header>
  <div class="abs brand">
    <span class="brand-mark"></span>
    <span class="brand-name">Maple Lane<br>Cafe &amp; Market</span>
  </div>
  <div class="abs account">CREATE AN ACCOUNT<span>|</span>SIGN UP</div>
  <nav class="abs nav">
    <a>HOME</a><a>EVENTS</a><a>CAFE MENU</a><a>MARKETPLACE PRODUCTS</a><a>HEALTH INFO</a><a>NEWS</a><a>RECIPES</a><a>CONTACT US</a>
  </nav>
</header>

<section>
  <div class="abs hero" role="img" aria-label="Smiling woman giving a thumbs up beside fresh fruit and vegetables"></div>
  <div class="abs hero-band"></div>
  <h1 class="abs hero-title">HIGHEST QUALITY, FRESH AND NATURAL FOOD</h1>
  <p class="abs hero-sub">health and wellness products</p>
  <div class="btn" style="left:544px;top:653px;width:112px;height:41px;font-size:16px">Read More</div>
  <div class="abs dots"><i></i><i class="on"></i><i></i></div>
</section>

<section>
  <div class="abs feature-panel"></div>
  <h2 class="section-title" style="top:796px">OUR FEATURE</h2>
  <div class="photo" style="left:60px;top:870px;width:299px;height:176px;background:radial-gradient(circle at 30% 40%,#d23a2a,#8a6a3a 45%,#4e7a2c 80%)" role="img" aria-label="Crates of organic vegetables"></div>
  <div class="photo" style="left:450px;top:870px;width:299px;height:176px;background:radial-gradient(circle at 50% 50%,#c9b98a,#7a5434 50%,#4a2e1b)" role="img" aria-label="Natural ingredients in bowls on wood"></div>
  <div class="photo" style="left:839px;top:870px;width:299px;height:176px;background:radial-gradient(circle at 50% 60%,#e0a84a,#c4602a 45%,#f2eee6 80%)" role="img" aria-label="Pasta, oil and vegetables"></div>
  <div class="abs feature-label" style="left:60px">Organic</div>
  <div class="abs feature-label" style="left:450px">Natural</div>
  <div class="abs feature-label" style="left:839px">Healthy</div>
  <div class="abs rule" style="top:1129px"></div>
</section>

<section>
  <h2 class="section-title" style="top:1173px">FEATURED PRODUCTS</h2>
  <div class="photo" style="left:60px;top:1251px;width:261px;height:185px;background:radial-gradient(circle at 60% 50%,#f0a020,#c0282a 50%,#3f7a2c)" role="img" aria-label="Assorted vegetables and citrus"></div>
  <div class="photo" style="left:335px;top:1251px;width:261px;height:185px;background:radial-gradient(circle at 50% 55%,#e8e2d2,#e8702a 50%,#5f9a38)" role="img" aria-label="Carrots, cucumber and greens"></div>
  <div class="photo" style="left:609px;top:1251px;width:261px;height:185px;background:radial-gradient(circle at 50% 70%,#e8611f,#e9c2a0 50%,#8cc24f)" role="img" aria-label="Woman holding fresh produce"></div>
  <div class="photo" style="left:881px;top:1251px;width:261px;height:185px;background:radial-gradient(circle at 60% 70%,#f08a1c,#c55a1f 45%,#5a1e2a)" role="img" aria-label="Market stall of fruit"></div>

  <div class="abs product-name" style="left:60px">Organic Garden Vegetable<br>Box, picked this week</div>
  <div class="abs product-name" style="left:335px">Local Farm Root &amp; Salad<br>Bundle, chemical-free</div>
  <div class="abs product-name" style="left:609px">Fresh Seasonal Fruit Bag,<br>grown near Lewiston</div>
  <div class="abs product-name" style="left:881px">Orchard Citrus &amp; Berry<br>Crate, ripe and sweet</div>
  <div class="abs product-price" style="left:60px">$4.95</div>
  <div class="abs product-price" style="left:335px">$4.95</div>
  <div class="abs product-price" style="left:609px">$4.95</div>
  <div class="abs product-price" style="left:881px">$4.95</div>
  <div class="btn" style="left:60px;top:1544px;width:257px;height:46px">View Details</div>
  <div class="btn" style="left:335px;top:1544px;width:257px;height:46px">View Details</div>
  <div class="btn" style="left:609px;top:1544px;width:257px;height:46px">View Details</div>
  <div class="btn" style="left:881px;top:1544px;width:257px;height:46px">View Details</div>
</section>

<section>
  <div class="abs welcome"></div>
  <h2 class="section-title" style="top:1679px">WELCOME TO MAPLE LANE CAFE &amp; MARKET</h2>
  <div class="abs video" role="img" aria-label="Video still of dry penne pasta in a copper bowl"></div>
  <div class="abs video-side" style="top:1775px"><svg width="16" height="14" viewBox="0 0 16 14"><path d="M8 13 1.5 6.5A3.5 3.5 0 0 1 8 2a3.5 3.5 0 0 1 6.5 4.5Z" fill="#fff"/></svg></div>
  <div class="abs video-side" style="top:1811px"><svg width="16" height="16" viewBox="0 0 16 16"><circle cx="8" cy="8" r="6.5" fill="none" stroke="#fff" stroke-width="1.6"/><path d="M8 4v4l3 2" stroke="#fff" stroke-width="1.6" fill="none"/></svg></div>
  <div class="abs video-side" style="top:1847px"><svg width="16" height="16" viewBox="0 0 16 16"><circle cx="4" cy="8" r="2" fill="#fff"/><circle cx="12" cy="3" r="2" fill="#fff"/><circle cx="12" cy="13" r="2" fill="#fff"/><path d="M4 8 12 3M4 8l8 5" stroke="#fff" stroke-width="1.4"/></svg></div>
  <div class="abs video-side" style="top:1883px"><svg width="18" height="12" viewBox="0 0 18 12"><path d="M5 1 1 6l4 5M13 1l4 5-4 5M10 0 8 12" stroke="#fff" stroke-width="1.6" fill="none"/></svg></div>
  <div class="abs video-bar"></div>
  <svg class="abs" style="left:90px;top:2018px" width="16" height="18" viewBox="0 0 16 18"><path d="M1 1 15 9 1 17Z" fill="#fff"/></svg>
  <div class="abs video-track"></div>
  <div class="abs video-fill"></div>
  <div class="abs" style="left:505px;top:2018px;font-size:12px;font-weight:600;color:var(--teal-light);font-style:italic">HD</div>

  <h3 class="abs welcome-head">A neighborhood market and cafe for real food. Fresh,<br>local and organic, every single day.</h3>
  <p class="abs welcome-copy" style="top:1830px">We bring organic, locally grown produce and preservative-free groceries to the heart of Birchwood Avenue.</p>
  <p class="abs welcome-copy" style="top:1898px">Our kitchen serves healthy lunch and dinner made from whole foods, sourced from nearby farms whenever we can. Stop in for a meal, shop the market, or pick up body care and eco-household goods.</p>
  <div class="btn" style="left:596px;top:1994px;width:114px;height:42px;font-size:16px">Read More</div>
</section>

<section>
  <h2 class="section-title" style="top:2133px">CLIENT TESTIMONIAL</h2>
  <div class="abs avatar" role="img" aria-label="Portrait of the client"></div>
  <div class="abs quote-mark">&ldquo;</div>
  <p class="abs quote-text">Maple Lane has become our weekly stop. The produce is always fresh, the staff know where every item comes from, and the cafe lunches are healthy and delicious. It is exactly the natural food store our town was missing.</p>
  <div class="abs quote-name">Nora Vale</div>
</section>

<footer>
  <div class="abs footer"></div>
  <h4 class="abs foot-head" style="left:60px">Menu</h4>
  <ul class="abs foot-list" style="left:60px"><li>Home</li><li>Events</li><li>Cafe Menu</li><li>Health Info</li></ul>
  <h4 class="abs foot-head" style="left:248px">Main Menu</h4>
  <ul class="abs foot-list" style="left:248px"><li>Marketplace Products</li><li>News</li><li>Recipes</li><li>Contact Us</li></ul>
  <h4 class="abs foot-head" style="left:457px">Newsletter:</h4>
  <div class="abs mail-input">Enter your Mail ID</div>
  <div class="btn" style="left:707px;top:2485px;width:101px;height:40px;font-size:17px">Sign up</div>
  <h4 class="abs foot-head" style="left:912px">Follow Us</h4>
  <div class="abs social"><i></i><i></i><i></i><i></i><i></i><i></i><i></i></div>
  <div class="abs copyright-bar"></div>
  <div class="abs copyright">Copyright©2015 Maple Lane Cafe &amp; Market</div>
</footer>

</body>
</html>
```